Business Cards for a Firearms Business - Corvane Works

Corvane Works manufactures, distributes and retails firearms parts. I am looking for someone to use the logos that I have provided to design some business cards that show that we're a modern, industrial, design focused and tactical business.

Look at [url removed, login to view] for examples of the type of branding that I am looking to emulate.

These will be a standard business card on standard cardstock paper. Nothing special here about the dimensions or materials.

On the front of the card, use either the logos that I am providing, or do some slight modifications to these logos to fit the design that looks the best. Feel free to pick the one that you like, or that will fit what you're trying to do the best here. Take artistic liberty to make this card pop. I do not want any contact information on the front of the card, only the company logo.

On the back of the card I would like the contact information. Please use fictitious contact information for now, and make the background look cool somehow.

```html
<!DOCTYPE html>
<html lang="en">
<head>
<meta charset="utf-8">
<title>Corvane Works – Business Cards</title>
<link rel="stylesheet" href="https://fonts.googleapis.com/css2?family=Source+Sans+3:wght@400&display=swap">
<style>
  :root {
    --page: #e9e6e1;
    --card: #2a2626;
    --accent: #e8731e;
    --white: #ffffff;
    --muted: #d9d5d2;
  }
  * { box-sizing: border-box; margin: 0; padding: 0; }
  html, body {
    width: 1200px; height: 1025px; overflow: hidden;
    background: var(--page);
    font-family: "Source Sans 3", "Myriad Pro", sans-serif;
  }
  .sheet {
    width: 1200px; height: 1025px;
    display: flex; justify-content: center; align-items: center; gap: 40px;
  }
  .card {
    position: relative;
    width: 470px; height: 760px;
    background: var(--card);
    border-left: 16px solid var(--accent);
    border-right: 16px solid var(--accent);
    box-shadow: 0 6px 18px rgba(0,0,0,.25);
    overflow: hidden;
  }
  .brand {
    position: absolute; left: 0; right: 0;
    display: flex; align-items: center; justify-content: center; gap: 14px;
  }
  .brand__mark { flex: none; background: var(--accent); }
  .brand__name { color: var(--white); font-weight: 400; white-space: nowrap; }

  /* contact side */
  .card--contact .brand { top: 105px; }
  .card--contact .brand__mark { width: 22px; height: 22px; }
  .card--contact .brand__name { font-size: 42px; }
  .person { position: absolute; left: 38px; top: 308px; }
  .person__name { color: var(--muted); font-size: 31px; font-weight: 400; }
  .person__role { color: var(--accent); font-size: 19px; font-weight: 400; margin-top: 6px; }
  .divider {
    position: absolute; left: 0; right: 0; top: 400px; height: 2px;
    background: linear-gradient(90deg, rgba(232,115,30,.2), var(--accent) 50%, rgba(232,115,30,.2));
  }
  .contacts { position: absolute; left: 34px; top: 492px; list-style: none; }
  .contacts li {
    display: flex; align-items: center; gap: 18px;
    color: var(--white); font-size: 20px; height: 48px;
  }
  .contacts svg { width: 28px; height: 28px; flex: none; }

  /* brand side */
  .card--brand .brand { top: 50%; transform: translateY(-50%); }
  .card--brand .brand__mark { width: 28px; height: 28px; }
  .card--brand .brand__name { font-size: 50px; }
</style>
</head>
<body>
<main class="sheet">
  <section class="card card--contact">
    <div class="brand">
      <span class="brand__mark"></span>
      <span class="brand__name">Corvane Works</span>
    </div>
    <div class="person">
      <p class="person__name">Prename Name</p>
      <p class="person__role">Creative Director</p>
    </div>
    <div class="divider"></div>
    <ul class="contacts">
      <li>
        <svg viewBox="0 0 28 28" aria-hidden="true"><rect x="8" y="2" width="13" height="24" rx="2" fill="var(--accent)"/><rect x="10.5" y="5" width="8" height="7" fill="var(--card)"/><g fill="var(--card)"><rect x="10.5" y="14" width="2" height="2"/><rect x="13.5" y="14" width="2" height="2"/><rect x="16.5" y="14" width="2" height="2"/><rect x="10.5" y="17.5" width="2" height="2"/><rect x="13.5" y="17.5" width="2" height="2"/><rect x="16.5" y="17.5" width="2" height="2"/><rect x="10.5" y="21" width="2" height="2"/><rect x="13.5" y="21" width="2" height="2"/><rect x="16.5" y="21" width="2" height="2"/></g></svg>
        +61 400 555 018
      </li>
      <li>
        <svg viewBox="0 0 28 28" aria-hidden="true"><rect x="3" y="7" width="22" height="15" rx="1.5" fill="var(--accent)"/><path d="M3.5 8 L14 16 L24.5 8" fill="none" stroke="var(--card)" stroke-width="1.8"/></svg>
        name@corvane.works
      </li>
      <li>
        <svg viewBox="0 0 28 28" aria-hidden="true"><circle cx="14" cy="14" r="11" fill="var(--accent)"/><g fill="none" stroke="var(--card)" stroke-width="1.3"><ellipse cx="14" cy="14" rx="5" ry="11"/><line x1="3" y1="14" x2="25" y2="14"/><line x1="14" y1="3" x2="14" y2="25"/><path d="M5 8.5 H23 M5 19.5 H23"/></g></svg>
        corvaneworks.com.au
      </li>
    </ul>
  </section>

  <section class="card card--brand">
    <div class="brand">
      <span class="brand__mark"></span>
      <span class="brand__name">Corvane Works</span>
    </div>
  </section>
</main>
</body>
</html>
```